Finance Company Need Presentation Folder/ Brochure Design

We are a Finance Brokerage Firm in Adelaide, we provide finance for personal, car, equipment, boat and aviation loans. We are looking for designs for new presentation folders that are simplistic, yet professional and classy. We would like them to include the color orange and communicate financial safety and growth.

Target Market(s)

The folders will be going to current and perspective clients

Industry/Entity Type

Finance

Font styles to use
Other font styles liked:
• Raleway or something similar, example attached as 'Opening Keys Evening'

Colors
f37122
ffffff
000000

Requirements
Must have
• Phone Number: 1300 482 917
• Address:
• 47 Warrick Lane
• Brookhaven, SA 5071
• Website: tallowpeak.com.au
Nice to have
• "Experience finance in a whole new way... Experience Tallowpeak"
• Asset Finance - Home Loans - Personal Loans

```html
<!DOCTYPE html>
<html lang="en">
<head>
<meta charset="utf-8">
<title>Tallowpeak Presentation Folder</title>
<link href="https://fonts.googleapis.com/css2?family=Raleway:wght@300;400;600;700&display=swap" rel="stylesheet">
<style>
  :root {
    --orange: #f37122;
    --charcoal: #33363a;
    --charcoal-light: #4a4e53;
    --white: #ffffff;
    --paper: #f4f4f4;
    --backdrop: #e4e4e4;
    --label: #222222;
  }
  * { box-sizing: border-box; margin: 0; padding: 0; }
  html, body { width: 850px; height: 1200px; overflow: hidden; }
  body {
    background: radial-gradient(ellipse at 50% 40%, #f2f2f2 0%, var(--backdrop) 75%);
    font-family: "Raleway", sans-serif;
    position: relative;
  }
  .view-label {
    position: absolute;
    font-weight: 300;
    font-size: 26px;
    letter-spacing: 1px;
    color: var(--label);
  }
  .spread {
    position: absolute;
    left: 85px;
    width: 680px;
    height: 480px;
    display: flex;
    box-shadow: 0 18px 40px rgba(0,0,0,0.18);
  }
  .panel { position: relative; width: 340px; height: 480px; overflow: hidden; }
  .panel--dark-left { background: linear-gradient(135deg, var(--charcoal) 0%, var(--charcoal-light) 100%); }
  .panel--dark-right { background: linear-gradient(225deg, var(--charcoal-light) 0%, var(--charcoal) 100%); }
  .panel--white-left { background: linear-gradient(90deg, var(--white) 0%, var(--paper) 100%); }
  .panel--white-right { background: linear-gradient(90deg, #e9e9e9 0%, var(--white) 25%); }
  .fold { position: absolute; top: 0; bottom: 0; left: 339px; width: 2px; background: rgba(0,0,0,0.18); }

  .brand-name { font-weight: 300; color: var(--white); white-space: nowrap; }
  .brand-name--front { position: absolute; top: 34px; right: 28px; font-size: 30px; }
  .brand-name--back { position: absolute; left: 28px; bottom: 36px; font-size: 18px; }

  .contact-list {
    position: absolute; left: 112px; bottom: 70px;
    list-style: none; color: var(--white); font-size: 10px; line-height: 1.35;
  }
  .contact-list li { display: flex; align-items: flex-start; gap: 8px; margin-bottom: 2px; }
  .contact-list .phone { font-weight: 700; font-size: 12px; }
  .contact-list svg { flex: none; margin-top: 2px; }

  .tagline { position: absolute; right: 28px; bottom: 52px; text-align: right; color: var(--white); }
  .tagline__lead { color: var(--orange); font-size: 12px; font-weight: 400; }
  .tagline__sub { font-size: 12px; font-weight: 400; margin-bottom: 4px; }
  .tagline__experience { color: var(--orange); font-size: 24px; font-weight: 400; line-height: 1.05; }
  .tagline__name { font-size: 30px; font-weight: 300; line-height: 1.05; }
  .tagline__name strong { font-weight: 700; }
  .services {
    position: absolute; right: 28px; bottom: 26px;
    color: var(--white); font-size: 9px; font-weight: 600; letter-spacing: 0.3px;
  }
  .services .dot { color: var(--orange); margin: 0 4px; }

  .pocket {
    position: absolute; bottom: 0; height: 150px;
    background: linear-gradient(180deg, var(--charcoal-light) 0%, var(--charcoal) 100%);
  }
  .pocket--left { left: 0; width: 340px; border-top-right-radius: 26px; }
  .pocket--right { right: 0; width: 340px; border-top-left-radius: 26px; }
  .pocket .brand-name { position: absolute; left: 66px; top: 58px; font-size: 26px; }
  .business-card {
    position: absolute; left: 76px; top: 36px; width: 104px; height: 62px;
    background: var(--orange);
    display: flex; align-items: center; justify-content: center;
  }
  .business-card .brand-name { position: static; font-size: 12px; }
</style>
</head>
<body>
  <div class="view-label" style="left:150px; top:26px;">OUTSIDE</div>

  <section class="spread" style="top:76px;" aria-label="Folder outside">
    <div class="panel panel--dark-left">
      <ul class="contact-list">
        <li>
          <svg width="9" height="10" viewBox="0 0 10 10"><path d="M2 1l2 2-1 1.5c.6 1.2 1.3 1.9 2.5 2.5L7 6l2 2-1.5 1.5C4.5 9 1 5.5.5 2.5z" fill="var(--orange)"/></svg>
          <span class="phone">1300 482 917</span>
        </li>
        <li>
          <svg width="9" height="10" viewBox="0 0 10 10"><circle cx="5" cy="5" r="4" fill="none" stroke="var(--orange)" stroke-width="1.3"/><path d="M1 5h8M5 1v8" stroke="var(--orange)" stroke-width="0.8"/></svg>
          <span>www.tallowpeak.com.au</span>
        </li>
        <li>
          <svg width="9" height="11" viewBox="0 0 10 12"><path d="M5 0C2.5 0 1 1.8 1 4c0 3 4 8 4 8s4-5 4-8c0-2.2-1.5-4-4-4z" fill="var(--orange)"/><circle cx="5" cy="4" r="1.4" fill="var(--charcoal)"/></svg>
          <span>47 Warrick Lane Brookhaven,<br>South Australia 5071</span>
        </li>
      </ul>
      <div class="brand-name brand-name--back">Tallowpeak</div>
    </div>
    <div class="panel panel--dark-right">
      <div class="brand-name brand-name--front">Tallowpeak</div>
      <div class="tagline">
        <p class="tagline__lead">EXPERIENCE FINANCE</p>
        <p class="tagline__sub">IN A WHOLE NEW WAY...</p>
        <p class="tagline__experience">EXPERIENCE</p>
        <p class="tagline__name"><strong>TALLOW</strong>PEAK</p>
      </div>
      <p class="services">ASSET FINANCE<span class="dot">•</span>HOME LOANS<span class="dot">•</span>PERSONAL LOANS</p>
    </div>
    <div class="fold"></div>
  </section>

  <div class="view-label" style="left:150px; top:596px;">INSIDE</div>

  <section class="spread" style="top:646px;" aria-label="Folder inside">
    <div class="panel panel--white-left">
      <div class="pocket pocket--left">
        <div class="brand-name">Tallowpeak</div>
      </div>
    </div>
    <div class="panel panel--white-right">
      <div class="pocket pocket--right">
        <div class="business-card"><span class="brand-name">Tallowpeak</span></div>
      </div>
    </div>
    <div class="fold"></div>
  </section>
</body>
</html>
```